I am a coffee roaster. We import and sell some of the finest coffee you can buy.

I am needing a package design for coffee. Our coffee is some of the finest you can buy so I am wanting a packaging that shows that. I have our brand logo but really need the packaging created.

Estate Grown Arabica coffees from countries make up Moravik Select blends. Only a handful of the world’s premiere coffee beans can produce the flavor, richness, and aroma that make Moravik Select coffees stand out from traditionally grown coffees. Ingredients: Coffee Tavish-Ponbury Beverage 800-316-2758 www.tpbeverage.example

```html
<!DOCTYPE html>
<html lang="en">
<head>
<meta charset="UTF-8">
<title>Moravik Select – Dark Roast Ground Packaging</title>
<link href="https://fonts.googleapis.com/css2?family=Oswald:wght@400;500;600&family=Roboto+Condensed:wght@400&display=swap" rel="stylesheet">
<style>
  :root {
    --canvas: #ffffff;
    --bag: #231f20;
    --bag-top: #353334;
    --gold: #a36a2e;
    --gold-light: #c99b68;
    --cream: #f3ede4;
    --bean-dark: #2b1a10;
    --bean-mid: #5a3620;
    --bean-light: #8a5a35;
  }
  * { margin: 0; padding: 0; box-sizing: border-box; }
  html, body { width: 1200px; height: 1000px; overflow: hidden; background: var(--canvas); }
  .canvas { position: relative; width: 1200px; height: 1000px; background: var(--canvas); }

  .panel { position: absolute; top: 214px; height: 681px; background: var(--bag); }
  .side-panel { left: 489px; width: 180px; }
  .front-panel { left: 683px; width: 375px; overflow: hidden; }

  .side-copy {
    position: absolute; left: 25px; top: 305px; width: 140px;
    font-family: "Roboto Condensed", sans-serif; font-size: 9px; line-height: 13px;
    color: var(--gold-light);
  }

  .brand-name {
    position: absolute; font-family: "Oswald", sans-serif; font-weight: 400;
    color: var(--gold); text-transform: uppercase; white-space: nowrap;
    display: flex; align-items: center;
  }
  .brand-dot { display: inline-block; border-radius: 50%; background: var(--gold); }
  .side-brand { left: 18px; top: 574px; font-size: 19px; letter-spacing: 0.5px; }
  .side-brand .brand-dot { width: 12px; height: 12px; margin-right: 8px; }
  .front-brand { left: 45px; top: 150px; font-size: 33px; letter-spacing: 1px; }
  .front-brand .brand-dot { width: 20px; height: 20px; margin-right: 12px; }

  .top-band { position: absolute; left: 0; top: 0; width: 375px; height: 300px; }

  .product-title {
    position: absolute; left: 0; top: 300px; width: 375px; text-align: center;
    font-family: "Oswald", sans-serif; font-weight: 500; font-size: 46px; line-height: 50px;
    color: var(--gold); text-transform: uppercase; letter-spacing: 0.5px;
  }

  .cup-image {
    position: absolute; left: 105px; top: 410px; width: 170px; height: 110px;
    border-radius: 50% 50% 45% 45%;
    background: radial-gradient(ellipse at 50% 40%, #ffffff 0%, #e4e4e4 55%, rgba(35,31,32,0) 72%);
  }

  .bean-band {
    position: absolute; left: 40px; top: 544px; width: 295px; height: 137px;
    border-top: 6px solid var(--gold);
    background: linear-gradient(135deg, var(--bean-mid) 0%, var(--bean-dark) 35%, var(--bean-light) 60%, var(--bean-dark) 100%);
  }
  .bean-text {
    position: absolute; left: 0; width: 100%; text-align: center; color: var(--cream);
    font-family: "Oswald", sans-serif; text-transform: uppercase; white-space: nowrap;
  }
  .bean-headline { top: 26px; font-size: 21px; font-weight: 400; letter-spacing: 0.5px; }
  .bean-rule { position: absolute; left: 25px; top: 57px; width: 245px; height: 1px; background: var(--cream); }
  .bean-sub { top: 58px; font-size: 16px; font-weight: 400; }
  .net-weight { top: 92px; font-size: 18px; font-weight: 600; }
</style>
</head>
<body>
<main class="canvas">

  <section class="panel side-panel">
    <p class="side-copy">Roaster coffee varieties. is a great tasting coffee that is know worldwide. Which run from Top Rate 1 in 3 of coffee from around the world submitted entries. Has been proved that mountain range is very perfect for growing the best coffee in the world. Due to many factor, The terrain is 1,200 meters above sea level the climate is cool all year round and for cultivated soil in land is volcanic soil. The minerals that are suitable for growing the best coffee.</p>
    <div class="brand-name side-brand"><span class="brand-dot"></span>Moravik Select</div>
  </section>

  <section class="panel front-panel">
    <svg class="top-band" viewBox="0 0 375 300" aria-hidden="true">
      <path d="M40 0 H335 V268 C270 250 190 262 130 275 C95 282 65 288 40 290 Z" fill="var(--bag-top)"/>
      <path d="M40 290 C65 288 95 282 130 275 C190 262 270 250 335 268" fill="none" stroke="var(--gold)" stroke-width="4"/>
    </svg>
    <div class="brand-name front-brand"><span class="brand-dot"></span>Moravik Select</div>

    <h1 class="product-title">Dark Roast<br>Ground</h1>

    <div class="cup-image" role="img" aria-label="Photo of a steaming white cup of black coffee on a saucer with a spoon"></div>

    <div class="bean-band" role="img" aria-label="Photo of dark roasted coffee beans">
      <p class="bean-text bean-headline">100% Coffee Roaster</p>
      <span class="bean-rule"></span>
      <p class="bean-text bean-sub">Suitable for all coffee use</p>
      <p class="bean-text net-weight">Net Wt 12 oz</p>
    </div>
  </section>

</main>
</body>
</html>
```